Retail Package for Ammunition Company

We are looking for a packaging design for a retail boxed ammunition. The "look". Attached will be the logo to be used. The logo is attached and a can be manipulated on the box. Box to represent strength and accuracy. Will need to provide .psd files to allow in house personnel to add/remove text to other calibers and warnings. Wow me with your designs!

Browse Other Brands: http://www.brightfalconstore.com/brands

The packaging needs to include:
Logo- provided and the following text:

FRONT 1. 9mm 115gr FMJ

BACK 2. WARNING: To avoid serious injury: (1) use only ammunition in good condition; use only in modern firearms in good condition marked for .22 Long Rifle (LR) cartridges; (2) always be sure barrel is free of any obstructions; the barrel should be checked in case of light recoil, or an unusually loud or weak sound heard during firing; (3) wear eye and ear protection; (4) if gun fails to fire, avoid exposure to breech when unloading and point muzzle in a safe direction. Keep firearm pointed in safe direction at all times; (5) discharge may occur if rim is struck; handle with caution, do not drop. (6) Do not shoot at hard surfaces or water to prevent ricochet; (7) Bullet is capable of traveling extreme distances. Know your backstop; (8) Store in cool dry place

3. LEAD WARNING: Discharging firearms in poorly ventilated areas, cleaning firearms, or handling ammunition may result in exposure to lead and other substances known to cause birth defects, reproductive harm, and other serious physical injury. Have adequate ventilation at all times. Wash hands thoroughly after exposure.

Dimensions ; (LxWxH): 5.25" x 2.625" x 1.125"

Target Market(s)

Ammunition Industry

```html
<!DOCTYPE html>
<html lang="en">
<head>
<meta charset="utf-8">
<title>Crimson Kestrel Arms – 9mm Retail Box Dieline</title>
<link href="https://fonts.googleapis.com/css2?family=Nunito+Sans:wght@400;700;800&family=Saira:ital,wght@1,800&display=swap" rel="stylesheet">
<style>
  :root{
    --backdrop:#181818;
    --panel-black:#050505;
    --brand-red:#c8141c;
    --band-red:#9e2a30;
    --band-red-light:#b0474c;
    --metal-dark:#4a4a4a;
    --metal-mid:#8a8a8a;
    --metal-light:#b4b4b4;
    --perf-dark:#2e2e2e;
    --perf-light:#9a9a9a;
    --white:#ffffff;
  }
  *{box-sizing:border-box;margin:0;padding:0}
  html,body{width:1200px;height:1034px;overflow:hidden;background:var(--backdrop)}
  body{position:relative;font-family:"Nunito Sans",Arial,sans-serif}
  .part{position:absolute}
  .perforated{background:radial-gradient(circle at 50% 40%,var(--perf-light),var(--perf-dark) 140%)}
  .brushed-metal{background:linear-gradient(100deg,var(--metal-dark),var(--metal-mid) 30%,var(--metal-light) 55%,var(--metal-mid) 75%,var(--metal-dark))}
  .front-face{left:142px;top:62px;width:188px;height:219px;background:radial-gradient(ellipse at 40% 20%,#3a3a3a,var(--panel-black) 60%,#1c1c1c);text-align:center}
  .brand-mark{position:absolute;left:0;right:0;top:70px;display:flex;flex-direction:column;align-items:center;gap:8px}
  .brand-dot{width:22px;height:22px;border-radius:50%;background:var(--brand-red)}
  .brand-name{color:var(--brand-red);font-weight:800;font-size:17px;letter-spacing:1px;line-height:1.05}
  .caliber{position:absolute;left:0;right:0;top:167px;color:var(--white);font-family:"Saira",Arial,sans-serif;font-style:italic;font-weight:800;font-size:14.5px;letter-spacing:.5px}
  .front-wordmark{position:absolute;left:0;right:0;top:192px;color:var(--brand-red);font-weight:700;font-size:11px;letter-spacing:1px}
  .red-band{left:142px;top:281px;width:188px;height:79px;background:radial-gradient(ellipse at 40% 25%,var(--band-red-light),var(--band-red) 70%)}
  .side-wordmark{position:absolute;top:26px;display:flex;align-items:center;gap:6px;color:var(--brand-red);font-weight:800;font-size:13px;letter-spacing:.5px}
  .side-wordmark .brand-dot{width:14px;height:14px}
  .lead-warning{left:636px;top:295px;width:279px;height:50px;background:var(--panel-black);border-radius:12px;padding:5px 14px;color:var(--brand-red);font-size:5.6px;line-height:1.38;text-align:center}
  .lead-warning b,.back-warning b{font-weight:800}
  .back-face{left:644px;top:360px;width:254px;height:219px;background:var(--panel-black);padding:32px 17px 0 17px;color:var(--brand-red)}
  .back-warning .intro{font-size:7.5px;margin-bottom:8px}
  .back-warning ul{list-style:none}
  .back-warning li{position:relative;padding-left:12px;font-size:4.6px;line-height:1.45;margin-bottom:8px}
  .back-warning li::before{content:"";position:absolute;left:1px;top:2px;width:2px;height:2px;border-radius:50%;background:var(--brand-red)}
</style>
</head>
<body>
  <!-- front panel -->
  <div class="part perforated" style="left:54px;top:62px;width:88px;height:219px" role="img" aria-label="Perforated steel plate texture"></div>
  <div class="part perforated" style="left:330px;top:62px;width:84px;height:219px" role="img" aria-label="Perforated steel plate texture"></div>
  <div class="part front-face">
    <div class="brand-mark">
      <span class="brand-dot"></span>
      <span class="brand-name">CRIMSON<br>KESTREL</span>
    </div>
    <div class="caliber">1. 9mm 115gr FMJ</div>
    <div class="front-wordmark">CRIMSON KESTREL ARMS</div>
  </div>

  <!-- side strip -->
  <div class="part brushed-metal" style="left:54px;top:281px;width:88px;height:79px" role="img" aria-label="Brushed scratched metal texture"></div>
  <div class="part red-band"></div>
  <div class="part brushed-metal" style="left:330px;top:281px;width:804px;height:79px" role="img" aria-label="Brushed scratched metal texture"></div>
  <div class="part side-wordmark" style="left:437px;top:307px;position:absolute"><span class="brand-dot"></span>CRIMSON KESTREL</div>
  <div class="part side-wordmark" style="left:988px;top:307px;position:absolute"><span class="brand-dot"></span>CRIMSON KESTREL</div>
  <div class="part lead-warning"><b>LEAD WARNING:</b> Discharging firearms in poorly ventilated areas, cleaning firearms, or handling ammunition may result in exposure to lead and other substances known to cause birth defects, reproductive harm, and other serious physical injury. Have adequate ventilation at all times. Wash hands thoroughly after exposure.</div>

  <!-- back panel -->
  <div class="part perforated" style="left:594px;top:360px;width:50px;height:219px" role="img" aria-label="Perforated steel plate texture"></div>
  <div class="part perforated" style="left:898px;top:360px;width:59px;height:219px" role="img" aria-label="Perforated steel plate texture"></div>
  <div class="part back-face">
    <div class="back-warning">
      <p class="intro"><b>WARNING:</b> To avoid serious injury:</p>
      <ul>
        <li>(1) use only ammunition in good condition; use only in modern firearms in good condition marked for .22 Long Rifle (LR) cartridges;</li>
        <li>(2) always be sure barrel is free of any obstructions; the barrel should be checked in case of light recoil, or an unusually loud or weak sound heard during firing;</li>
        <li>(3) wear eye and ear protection;</li>
        <li>(4) if gun fails to fire, avoid exposure to breech when unloading and point muzzle in a safe direction. Keep firearm pointed in safe direction at all times;</li>
        <li>(5) discharge may occur if rim is struck; handle with caution, do not drop. (6) Do not shoot at hard surfaces or water to prevent ricochet; (7) Bullet is capable of traveling extreme distances. Know your backstop; (8) Store in cool dry place</li>
      </ul>
    </div>
  </div>
</body>
</html>
```